Agribusiness Insurance

I would like postcard designed to attract farmers and agribusiness owners to my insurance consulting services. My business model is being a Trusted Advisor through identifying exposures, developing strategies, implementing programs and then monitoring our designed plan. I am knowledge representative (13YRs ag insurance), Represent 15 Farm + Carriers (favorable pricing/competitive multiple options) Specialized in Confinements, Cattle Farms, and Grain Producers. No Membership Fees Necessary

Many Insurance Producers in my area are nearing retirement I am 33 and am looking to promote this..

Target Market(s)

Farmers and Agribusiness Owners

Industry/Entity Type

Agribusiness

Requirements
Must have

• Toby Halvern
Phone: Cell 555 207 4816
Email: thalvern@ruralplexadvice.example

```html
<!DOCTYPE html>
<html lang="en">
<head>
<meta charset="utf-8">
<title>Agricultural Insurance Postcard – Toby Halvern</title>
<link rel="stylesheet" href="https://fonts.googleapis.com/css2?family=Arvo:wght@400;700&family=Oswald:wght@500&family=Questrial&display=swap">
<style>
  :root {
    --leaf: #98ad4c;
    --moss: #56692c;
    --barn: #c11f27;
    --white: #ffffff;
    --ink: #111111;
    --field-green: #6f9a3a;
    --field-straw: #b89a62;
    --sky: #b9cfe0;
    --studio: #8e8378;
  }
  html, body {
    margin: 0;
    padding: 0;
    width: 1200px;
    height: 930px;
    overflow: hidden;
    background: var(--white);
  }
  .postcard {
    position: relative;
    width: 1200px;
    height: 930px;
    overflow: hidden;
    background: var(--leaf);
  }
  .backdrop {
    position: absolute;
    inset: 0;
  }
  .headline {
    position: absolute;
    left: 376px;
    top: 44px;
    margin: 0;
    font-family: "Questrial", sans-serif;
    font-weight: 400;
    font-size: 41px;
    letter-spacing: 0.2px;
    color: var(--ink);
    white-space: nowrap;
  }
  .headline-rule {
    position: absolute;
    left: 376px;
    top: 103px;
    width: 824px;
    height: 4px;
    background: var(--ink);
  }
  .question {
    position: absolute;
    right: 40px;
    top: 166px;
    margin: 0;
    font-family: "Arvo", serif;
    font-weight: 700;
    font-size: 41px;
    letter-spacing: 1px;
    color: var(--white);
    white-space: nowrap;
  }
  .needs {
    position: absolute;
    right: 40px;
    top: 240px;
    margin: 0;
    padding: 0;
    list-style: none;
    text-align: right;
    font-family: "Oswald", sans-serif;
    font-weight: 500;
    font-size: 35px;
    line-height: 42px;
    color: var(--white);
    letter-spacing: 0.5px;
  }
  .needs li {
    margin-bottom: 16px;
  }
  .needs li.two-line {
    margin-bottom: 22px;
  }
  .needs .arrow {
    display: inline-block;
    width: 20px;
    height: 20px;
    margin-right: 12px;
    vertical-align: 4px;
  }
  .badge-text {
    position: absolute;
    text-align: center;
    line-height: 1.15;
  }
  .no-fees {
    left: 240px;
    top: 588px;
    width: 180px;
    font-family: "Arvo", serif;
    color: var(--barn);
    font-size: 23px;
  }
  .no-fees strong {
    font-size: 26px;
    font-weight: 700;
  }
  .experience {
    left: 855px;
    top: 650px;
    width: 200px;
    font-family: "Arvo", serif;
    font-weight: 700;
    color: var(--white);
    font-size: 24px;
    line-height: 1.35;
  }
  .experience .years-number {
    font-size: 32px;
    display: block;
  }
  .contact {
    position: absolute;
    left: 400px;
    top: 676px;
    width: 450px;
    text-align: center;
    color: var(--white);
  }
  .contact-lead {
    margin: 0;
    font-family: "Questrial", sans-serif;
    font-size: 28px;
    color: var(--ink);
  }
  .contact-name {
    margin: 12px 0 0;
    font-family: "Arvo", serif;
    font-weight: 700;
    font-size: 35px;
    letter-spacing: 1px;
  }
  .contact-phone {
    margin: 12px 0 0;
    font-family: "Arvo", serif;
    font-weight: 700;
    font-size: 31px;
  }
  .contact-email {
    position: absolute;
    left: 280px;
    top: 836px;
    width: 690px;
    margin: 0;
    text-align: center;
    font-family: "Arvo", serif;
    font-size: 24px;
    color: var(--white);
    white-space: nowrap;
  }
</style>
</head>
<body>
<main class="postcard">
  <svg class="backdrop" width="1200" height="930" viewBox="0 0 1200 930" aria-hidden="false">
    <defs>
      <linearGradient id="harvest-tone" x1="0" y1="0" x2="0" y2="1">
        <stop offset="0" stop-color="#c9d8e6"/>
        <stop offset="0.45" stop-color="#a7b8c4"/>
        <stop offset="0.55" stop-color="#9c8560"/>
        <stop offset="1" stop-color="#7c6a45"/>
      </linearGradient>
      <linearGradient id="sprayer-tone" x1="0" y1="0" x2="0" y2="1">
        <stop offset="0" stop-color="#7fa84a"/>
        <stop offset="1" stop-color="#5e8a34"/>
      </linearGradient>
      <linearGradient id="cart-tone" x1="0" y1="0" x2="0" y2="1">
        <stop offset="0" stop-color="#3f86d0"/>
        <stop offset="0.5" stop-color="#b23a36"/>
        <stop offset="1" stop-color="#caa869"/>
      </linearGradient>
      <radialGradient id="portrait-tone" cx="0.5" cy="0.45" r="0.6">
        <stop offset="0" stop-color="#a59a8e"/>
        <stop offset="1" stop-color="#6e655c"/>
      </radialGradient>
    </defs>

    <!-- harvest field photo area -->
    <polygon class="photo-harvest" role="img" aria-label="Photo: combine harvesting a corn field beside a grain cart under a pale sky"
             points="0,150 300,190 640,600 60,930 0,930" fill="url(#harvest-tone)"/>

    <!-- diagonal stripes -->
    <polygon class="stripe-moss" points="318,150 372,150 1200,860 1200,905" fill="var(--moss)"/>
    <polygon class="stripe-white" points="290,190 318,150 1200,905 1200,935" fill="var(--white)"/>

    <!-- red contact panel -->
    <polygon class="panel-barn" points="40,930 470,588 760,588 1200,930" fill="var(--barn)"/>

    <!-- sprayer photo circle -->
    <circle cx="150" cy="100" r="152" fill="var(--white)"/>
    <circle class="photo-sprayer" role="img" aria-label="Photo: tractor spraying rows of green crops" cx="150" cy="100" r="143" fill="url(#sprayer-tone)"/>

    <!-- grain cart photo circle -->
    <circle cx="136" cy="800" r="108" fill="var(--white)"/>
    <circle class="photo-cart" role="img" aria-label="Photo: red tractor pulling a grain cart across a stubble field" cx="136" cy="800" r="100" fill="url(#cart-tone)"/>

    <!-- advisor portrait circle -->
    <circle cx="600" cy="465" r="176" fill="var(--white)"/>
    <circle class="photo-portrait" role="img" aria-label="Portrait photo of the insurance advisor in a dark suit and red shirt" cx="600" cy="465" r="166" fill="url(#portrait-tone)"/>

    <!-- badges -->
    <circle class="badge-no-fees" cx="330" cy="665" r="100" fill="var(--white)"/>
    <circle cx="955" cy="720" r="108" fill="var(--white)"/>
    <circle class="badge-experience" cx="955" cy="720" r="101" fill="var(--moss)"/>
  </svg>

  <h1 class="headline">Experts in Agricultural Insurance</h1>
  <div class="headline-rule"></div>

  <h2 class="question">ARE YOU LOOKINF FOR:</h2>
  <ul class="needs">
    <li><svg class="arrow" viewBox="0 0 20 20"><circle cx="10" cy="10" r="8.5" fill="none" stroke="#fff" stroke-width="2"/><path d="M8 6l4 4-4 4" fill="none" stroke="#fff" stroke-width="2"/></svg>A NEW FARM CARRIER?</li>
    <li class="two-line"><svg class="arrow" viewBox="0 0 20 20"><circle cx="10" cy="10" r="8.5" fill="none" stroke="#fff" stroke-width="2"/><path d="M8 6l4 4-4 4" fill="none" stroke="#fff" stroke-width="2"/></svg>A KNOWLEDGEABLE<br>REPRESENTATIVE?</li>
    <li><svg class="arrow" viewBox="0 0 20 20"><circle cx="10" cy="10" r="8.5" fill="none" stroke="#fff" stroke-width="2"/><path d="M8 6l4 4-4 4" fill="none" stroke="#fff" stroke-width="2"/></svg>LOWER PREMIUMS?</li>
    <li><svg class="arrow" viewBox="0 0 20 20"><circle cx="10" cy="10" r="8.5" fill="none" stroke="#fff" stroke-width="2"/><path d="M8 6l4 4-4 4" fill="none" stroke="#fff" stroke-width="2"/></svg>MORE OPTIONS?</li>
    <li><svg class="arrow" viewBox="0 0 20 20"><circle cx="10" cy="10" r="8.5" fill="none" stroke="#fff" stroke-width="2"/><path d="M8 6l4 4-4 4" fill="none" stroke="#fff" stroke-width="2"/></svg>BETTER SERVICE?</li>
  </ul>

  <div class="badge-text no-fees"><strong>No</strong><br>Membership<br>Fees<br>Necessary</div>
  <div class="badge-text experience"><span class="years-number">13+</span>years<br>experience</div>

  <section class="contact">
    <p class="contact-lead">Inquiry, Please Contact</p>
    <p class="contact-name">TOBY HALVERN</p>
    <p class="contact-phone">Tel: 555 207 4816</p>
  </section>
  <p class="contact-email">Email: thalvern@ruralplexadvice.example</p>
</main>
</body>
</html>
```